■コンペ内容
トップページをデザイン頂きます。1ページ(レスポンシブデザイン)
※当選の方のみ商品詳細ページをデザインして頂き、今回のコンペ終了とさせて頂きます。今回当選させて頂いた方には雑誌への広告紙面や、バナー、今後のサイトのコンテンツデザインなどを継続してお願いさせて頂けますと幸いです。長期的に良好な関係を築いていければと思っています。

■スケジュール(理想スケジュール)
11/16:デザイン決定を予定しております。
11/20:コーディング終了

トップページ
http://www.marlocove.jp/

商品詳細ページ
http://www.marlocove.jp/products/detail116.html

買取ページ
http://www.marlocove.jp/buy/

ブログ
http://www.marlocove.jp/blog/
http://www.marlocove.jp/
■重視する点
UI/UXを意識してデザインを行える方
操作を直感的に行えるUIデザインを考えることのできる方
ECサイトのデザインを行った事がある方

■禁止事項
他で登録されているデザインや商標の転用など、他社の知的財産権、著作権を侵すこと。その他何かご不明な点がございましたら、お気軽にご質問下さい。
よろしくお願いいたします。

<備考>
採用させて頂いたデザイン案をサイトに当て込む際に、
弊社側で多少デザインを変更する可能性がございますので、予めご了承ください。
https://www.filevantor.com/sh/zk83mp2wtrx7fa/BBxqPoLenWRTuvKcmZdYhGsQe?dl=0
全て使用して頂けます。
ご提案ありがとうございます。
もう少し延長させて頂きます。
明日には決定させますので、
何卒よろしくお願い致します。

レスポンシブを考えられたデザインが良かったです。

たくさんのご応募ありがとうございます。

```html
<!DOCTYPE html>
<html lang="ja">
<head>
<meta charset="utf-8">
<title>Marlo Cove</title>
<link href="https://fonts.googleapis.com/css2?family=Noto+Sans+JP:wght@400;700&family=Playfair+Display:wght@400;700&display=swap" rel="stylesheet">
<style>
:root{
  --cream:#f6f1e6;
  --paper:#fbf8f1;
  --ink:#3a2f2b;
  --muted:#8a7d75;
  --dark:#1d1a19;
  --rose:#c2566f;
  --wine:#8d1f2c;
  --lilac:#b9a0c9;
  --line:#d9cfc2;
  --pink:#f2c3cf;
}
*{box-sizing:border-box;margin:0;padding:0}
html,body{width:1200px;height:2356px;overflow:hidden}
body{background:var(--cream);font-family:"Noto Sans JP",sans-serif;color:var(--ink);font-size:12px;position:relative}
.header{height:120px;position:relative;background:linear-gradient(#efe6d4,var(--cream))}
.header-ornament{position:absolute;top:0;left:0;width:420px;height:110px;background:linear-gradient(90deg,#e4d6bd,rgba(228,214,189,0))}
.header-ornament.right{left:auto;right:0;background:linear-gradient(270deg,#e4d6bd,rgba(228,214,189,0))}
.logo{position:absolute;left:0;right:0;top:24px;text-align:center;font-family:"Playfair Display",serif;font-weight:700;font-size:44px;color:var(--wine);letter-spacing:1px}
.logo small{display:block;font-size:11px;font-weight:400;color:var(--wine);letter-spacing:3px;margin-top:-2px;font-family:"Playfair Display",serif}
.user-links{position:absolute;right:40px;top:14px;display:flex;gap:8px}
.user-links span{background:var(--dark);color:#fff;font-size:10px;padding:3px 10px}
.nav{height:22px;background:var(--dark);display:flex;justify-content:center;gap:46px;align-items:center}
.nav a{color:#eee;font-size:10px;text-decoration:none;letter-spacing:1px}
.hero{position:absolute;top:152px;left:100px;width:1000px;height:440px;background:linear-gradient(120deg,#e9c9c9 0%,#c79bb6 45%,#9a7aa4 70%,#e3c0c4 100%);border-top:6px solid #fff;border-bottom:6px solid #fff}
.sidebar{position:absolute;left:112px;top:632px;width:200px}
.box{background:#fff;border:1px solid var(--line);margin-bottom:20px}
.box-title{display:flex;align-items:center;gap:8px;padding:12px 12px;border-bottom:1px solid var(--line);font-family:"Playfair Display",serif;font-weight:700;font-size:16px;letter-spacing:1px}
.box-title i{width:26px;height:26px;border-radius:50%;background:var(--pink);display:block}
.list{list-style:none;padding:6px 14px 10px}
.list li{font-size:10.5px;padding:5px 0;border-bottom:1px dotted var(--line)}
.list li.sub{padding-left:14px;color:var(--muted)}
.search{padding:12px}
.search div{height:22px;border:1px solid var(--line);margin-bottom:8px;font-size:10px;color:var(--muted);padding:3px 6px}
.search b{display:block;width:70px;height:22px;background:var(--dark);color:#fff;font-size:10px;text-align:center;line-height:22px;font-weight:400}
.side-banner{height:56px;margin-bottom:10px}
.main{position:absolute;left:340px;top:620px;width:760px}
.cat-buttons{display:flex;gap:20px;height:52px}
.cat-buttons div{flex:1;display:flex;align-items:center;justify-content:center;color:#fff;font-family:"Playfair Display",serif;font-size:20px;letter-spacing:2px}
.lolita{background:linear-gradient(90deg,#b23a56,#d86a82)}
.gothic{background:linear-gradient(90deg,#2a2426,#4a3f42)}
.heading{display:flex;align-items:center;gap:10px;margin:40px 0 18px;font-family:"Playfair Display",serif;font-size:18px;font-weight:700;letter-spacing:1px}
.heading i{width:30px;height:30px;border-radius:50%;background:var(--pink);display:block}
.heading::after{content:"";flex:1;height:1px;background:var(--line)}
.grid{display:grid;grid-template-columns:repeat(5,136px);gap:20px 20px}
.card .photo{height:170px;border:1px solid var(--line)}
.card p{font-size:9.5px;line-height:1.5;margin-top:6px}
.card .brand{color:var(--muted);font-size:9px;margin-top:2px}
.card .price{color:var(--rose);font-weight:700;font-size:10px}
.c1{background:linear-gradient(#dcd6ea,#b5acd0)}
.c2{background:linear-gradient(#f4f1f4,#d8d0dc)}
.c3{background:linear-gradient(#f7d3dc,#eaa9ba)}
.c4{background:linear-gradient(#f6dfe5,#efbccb)}
.c5{background:linear-gradient(#a22a3a,#6c1420)}
.brands{display:grid;grid-template-columns:repeat(6,1fr);gap:10px}
.brand-tile .logo-box{height:64px;background:#fff;border:1px solid var(--line);display:flex;align-items:center;justify-content:center;text-align:center;font-family:"Playfair Display",serif;font-size:12px;color:var(--ink);padding:4px}
.brand-tile p{font-size:8.5px;color:var(--muted);margin-top:3px}
.page-top{position:absolute;left:1022px;top:2104px;width:76px;height:76px;border-radius:50%;background:var(--dark);color:#fff;font-size:9px;display:flex;align-items:center;justify-content:center;letter-spacing:1px;border:3px double #888}
.footer{position:absolute;left:0;bottom:0;width:1200px;height:170px;background:var(--dark);color:#ccc;text-align:center;padding-top:36px;font-size:10px}
.footer nav{display:flex;justify-content:center;gap:16px;margin-bottom:18px}
.footer .rule{width:300px;height:1px;background:#555;margin:0 auto 14px}
.footer small{font-size:9px;color:#999}
</style>
</head>
<body>
<header class="header">
  <div class="header-ornament" role="img" aria-label="アンティーク調の蝶と花の装飾"></div>
  <div class="header-ornament right" role="img" aria-label="アンティーク調の蝶と花の装飾"></div>
  <div class="logo">Marlo Cove<small>LOLITA &amp; GOTHIC</small></div>
  <div class="user-links"><span>ログイン</span><span>カート</span></div>
</header>
<nav class="nav">
  <a href="#">TOP</a><a href="#">LOLITA ITEM</a><a href="#">GOTHIC ITEM</a><a href="#">ABOUT</a><a href="#">BLOG</a><a href="#">CONTACT</a><a href="#">買取査定</a><a href="#">新規会員登録</a>
</nav>

<div class="hero" role="img" aria-label="薔薇と星空を背景にロリータ服をまとったモデルのメインビジュアル"></div>

<aside class="sidebar">
  <section class="box">
    <h2 class="box-title"><i></i>CATEGORY</h2>
    <ul class="list">
      <li>ジャンパースカート</li><li>ワンピース</li><li>トップス</li>
      <li class="sub">ブラウス</li><li class="sub">カットソー</li><li class="sub">ニット</li>
      <li>スカート</li><li>アウター</li><li>小物</li><li>バッグ・財布</li><li>シューズ</li><li>アクセサリー</li><li>その他</li>
    </ul>
  </section>
  <section class="box">
    <h2 class="box-title"><i></i>BRAND</h2>
    <ul class="list">
      <li>Seraphine Lace (42)</li><li>Starry Cradle (38)</li><li>Quiet Meadow (21)</li><li>Velvet Cream (17)</li><li>Clara &amp; the Corsairs (15)</li><li>Odette Garden (12)</li><li>k.ryusei (9)</li><li>Rosalind Vale (8)</li><li>Papillon Maison (7)</li><li>Noir Miroir (6)</li><li>Gaslight Maiden (5)</li><li>Posy Temple (4)</li><li>その他ブランド (11)</li>
    </ul>
  </section>
  <section class="box">
    <h2 class="box-title"><i></i>ITEM SERACH</h2>
    <div class="search"><div>キーワード</div><div>カテゴリーを選択</div><b>検索</b></div>
  </section>
  <div class="side-banner" style="background:linear-gradient(90deg,#cfe6ee,#f4d7e0)" role="img" aria-label="買取査定のご案内バナー"></div>
  <div class="side-banner" style="background:linear-gradient(90deg,#2a2426,#6a5a5e)" role="img" aria-label="ゴシックアイテム特集バナー"></div>
  <div class="side-banner" style="background:linear-gradient(90deg,#f6e6d2,#e7c7a9)" role="img" aria-label="ショップブログのバナー"></div>
</aside>

<main class="main">
  <div class="cat-buttons"><div class="lolita">LOLITA ITEM</div><div class="gothic">GOTHIC ITEM</div></div>

  <h2 class="heading"><i></i>PICK UP ITEM</h2>
  <div class="grid">
    <div class="card"><div class="photo c1" role="img" aria-label="ラベンダーのワンピース"></div><p>ミルキーリボンワンピース</p><p class="brand">Seraphine Lace</p><p class="price">¥18,000</p></div>
    <div class="card"><div class="photo c2" role="img" aria-label="白のジャンパースカート"></div><p>小花刺繍のフリルJSK</p><p class="brand">Seraphine Lace</p><p class="price">¥16,500</p></div>
    <div class="card"><div class="photo c3" role="img" aria-label="ピンクのカーディガン"></div><p>ピンクボレロ</p><p class="brand">Starry Cradle</p><p class="price">¥9,800</p></div>
    <div class="card"><div class="photo c4" role="img" aria-label="ピンクのケープ"></div><p>ピンクケープコート</p><p class="brand">Starry Cradle</p><p class="price">¥12,000</p></div>
    <div class="card"><div class="photo c5" role="img" aria-label="ワインレッドのジャンパースカート"></div><p>薔薇柄ベロアスカート</p><p class="brand">Starry Cradle</p><p class="price">¥14,000</p></div>
    <div class="card"><div class="photo c1" role="img" aria-label="ラベンダーのワンピース"></div><p>ミルキーリボンワンピース</p><p class="brand">Seraphine Lace</p><p class="price">¥18,000</p></div>
    <div class="card"><div class="photo c2" role="img" aria-label="白のジャンパースカート"></div><p>小花刺繍のフリルJSK</p><p class="brand">Seraphine Lace</p><p class="price">¥16,500</p></div>
    <div class="card"><div class="photo c3" role="img" aria-label="ピンクのカーディガン"></div><p>ピンクボレロ</p><p class="brand">Starry Cradle</p><p class="price">¥9,800</p></div>
    <div class="card"><div class="photo c4" role="img" aria-label="ピンクのケープ"></div><p>ピンクケープコート</p><p class="brand">Starry Cradle</p><p class="price">¥12,000</p></div>
    <div class="card"><div class="photo c5" role="img" aria-label="ワインレッドのジャンパースカート"></div><p>薔薇柄ベロアスカート</p><p class="brand">Starry Cradle</p><p class="price">¥14,000</p></div>
  </div>

  <h2 class="heading"><i></i>NEW ARRIVAL</h2>
  <div class="grid">
    <div class="card"><div class="photo c1" role="img" aria-label="ラベンダーのワンピース"></div><p>ミルキーリボンワンピース</p><p class="brand">Seraphine Lace</p><p class="price">¥18,000</p></div>
    <div class="card"><div class="photo c2" role="img" aria-label="白のジャンパースカート"></div><p>小花刺繍のフリルJSK</p><p class="brand">Velvet Cream</p><p class="price">¥16,500</p></div>
    <div class="card"><div class="photo c3" role="img" aria-label="ピンクのカーディガン"></div><p>ピンクボレロ</p><p class="brand">Starry Cradle</p><p class="price">¥9,800</p></div>
    <div class="card"><div class="photo c4" role="img" aria-label="ピンクのケープ"></div><p>ピンクケープコート</p><p class="brand">Starry Cradle</p><p class="price">¥12,000</p></div>
    <div class="card"><div class="photo c5" role="img" aria-label="ワインレッドのジャンパースカート"></div><p>薔薇柄ベロアスカート</p><p class="brand">Starry Cradle</p><p class="price">¥14,000</p></div>
  </div>

  <h2 class="heading"><i></i>BRAND</h2>
  <div class="brands">
    <div class="brand-tile"><div class="logo-box">Seraphine Lace</div><p>Seraphine Lace</p></div>
    <div class="brand-tile"><div class="logo-box">Starry Cradle</div><p>Starry Cradle</p></div>
    <div class="brand-tile"><div class="logo-box">Quiet Meadow</div><p>Quiet Meadow</p></div>
    <div class="brand-tile"><div class="logo-box">Velvet Cream</div><p>Velvet Cream</p></div>
    <div class="brand-tile"><div class="logo-box">Clara &amp; the Corsairs</div><p>Clara &amp; the Corsairs</p></div>
    <div class="brand-tile"><div class="logo-box">Odette Garden</div><p>Odette Garden</p></div>
    <div class="brand-tile"><div class="logo-box">k.ryusei</div><p>k.ryusei</p></div>
    <div class="brand-tile"><div class="logo-box">Rosalind Vale</div><p>Rosalind Vale</p></div>
    <div class="brand-tile"><div class="logo-box">Papillon Maison</div><p>Papillon Maison</p></div>
    <div class="brand-tile"><div class="logo-box">Noir Miroir</div><p>Noir Miroir</p></div>
    <div class="brand-tile"><div class="logo-box">Ivy Marlowe</div><p>Ivy Marlowe</p></div>
    <div class="brand-tile"><div class="logo-box">Colette et Celine</div><p>Colette et Celine</p></div>
    <div class="brand-tile"><div class="logo-box">Posy Temple</div><p>Posy Temple</p></div>
    <div class="brand-tile"><div class="logo-box">Gaslight Maiden</div><p>Gaslight Maiden</p></div>
    <div class="brand-tile"><div class="logo-box">Calm Hour</div><p>Calm Hour</p></div>
  </div>
</main>

<div class="page-top">PAGE TOP</div>

<footer class="footer">
  <nav><span>TOP</span><span>Marlo Coveについて</span><span>お問い合わせ</span><span>特定商取引法に基づく表記</span><span>プライバシーポリシー</span></nav>
  <div class="rule"></div>
  <small>Copyright © Marlo Cove. All Rights Reserved.</small>
</footer>
</body>
</html>
```